Tarnby Group letterhead

Hi,

I need a letterhead template created for our business. This should be done in word format and A4 size. The images need to not move in the template ie when I am adding writing in etc. and should flow on when I get to a second page.

I have attached our logo templates below.

Other details to include on the letterhead somewhere are:

0438 915 267
Max@Tarnbyelectrical.example.au
PO Box 817 Marrowvale NSW 2190
ABN: 57 318 962 407

Thanks!

```html
<!DOCTYPE html>
<html lang="en">
<head>
<meta charset="utf-8">
<title>Tarnby Group Letterhead</title>
<link href="https://fonts.googleapis.com/css2?family=Montserrat:wght@400;700&family=Arimo:wght@400&display=swap" rel="stylesheet">
<style>
  :root {
    --backdrop: #d0d0d0;
    --paper: #ffffff;
    --brand-orange: #f15a22;
    --ink: #231f20;
    --body-ink: #111111;
  }
  html, body {
    margin: 0;
    padding: 0;
    width: 1200px;
    height: 923px;
    overflow: hidden;
    background: var(--backdrop);
  }
  .letterhead {
    position: absolute;
    left: 287px;
    top: 23px;
    width: 625px;
    height: 877px;
    background: var(--paper);
    box-shadow: 0 2px 10px rgba(0,0,0,0.12);
  }
  .brand {
    position: absolute;
    left: 37px;
    top: 50px;
    width: 181px;
    text-align: center;
  }
  .brand-dot {
    width: 54px;
    height: 54px;
    margin: 0 auto 12px;
    border: 4px solid var(--ink);
    border-radius: 50%;
    box-sizing: border-box;
  }
  .brand-name {
    font-family: "Montserrat", sans-serif;
    font-weight: 700;
    font-size: 17px;
    letter-spacing: 0.5px;
    color: var(--ink);
    text-transform: uppercase;
    white-space: nowrap;
  }
  .contact {
    position: absolute;
    left: 368px;
    top: 64px;
    font-family: "Montserrat", sans-serif;
    font-size: 13px;
    color: var(--ink);
    list-style: none;
    margin: 0;
    padding: 0;
  }
  .contact li {
    display: flex;
    align-items: center;
    height: 20px;
    white-space: nowrap;
  }
  .contact svg {
    width: 12px;
    height: 12px;
    margin-right: 8px;
    fill: var(--brand-orange);
  }
  .contact .abn { padding-left: 2px; }
  .body-copy {
    position: absolute;
    left: 96px;
    top: 293px;
    width: 433px;
    font-family: "Arimo", Arial, sans-serif;
    font-size: 11.6px;
    line-height: 14px;
    color: var(--body-ink);
    text-align: justify;
  }
  .body-copy p { margin: 0; }
  .body-copy p + p { margin-top: 28px; }
</style>
</head>
<body>
  <main class="letterhead">
    <header>
      <div class="brand">
        <div class="brand-dot"></div>
        <div class="brand-name">Tarnby Group</div>
      </div>
      <ul class="contact">
        <li><svg viewBox="0 0 24 24"><path d="M6.6 10.8a15.1 15.1 0 0 0 6.6 6.6l2.2-2.2a1 1 0 0 1 1-.25 11.4 11.4 0 0 0 3.6.57 1 1 0 0 1 1 1V20a1 1 0 0 1-1 1A17 17 0 0 1 3 4a1 1 0 0 1 1-1h3.5a1 1 0 0 1 1 1c0 1.25.2 2.45.57 3.57a1 1 0 0 1-.25 1z"/></svg>0438 915 267</li>
        <li><svg viewBox="0 0 24 24"><path d="M2 5h20v14H2z M2 5l10 8 10-8" /></svg>Max@Tarnbyelectrical.example.au</li>
        <li><svg viewBox="0 0 24 24"><path d="M12 2a7 7 0 0 0-7 7c0 5.25 7 13 7 13s7-7.75 7-13a7 7 0 0 0-7-7zm0 9.5A2.5 2.5 0 1 1 12 6.5a2.5 2.5 0 0 1 0 5z"/></svg>PO Box 817 Marrowvale NSW 2190</li>
        <li class="abn">ABN: 57 318 962 407</li>
      </ul>
    </header>
    <section class="body-copy">
      <p>Lorem ipsum dolor sit amet, consectetur adipiscing elit. Donec fringilla neque euismod volutpat cursus. Vestibulum ac pretium orci, consequat elementum velit. Etiam bibendum purus ac augue finibus volutpat. Vestibulum justo nisl</p>
      <p>Lorem ipsum dolor sit amet, consectetur adipiscing elit. Donec fringilla neque euismod volutpat cursus. Vestibulum ac pretium orci, consequat elementum velit. Etiam bibendum purus ac augue finibus volutpat. Vestibulum justo nisl, gravida aliquet sollicitudin ut, finibus vitae mi. Praesent aliquet scelerisque blandit. Sed id varius lacus, id tristique sem. Fusce et lobortis leo. Aliquam mollis pellentesque magna, condimentum ullamcorper ex ullamcorper non. Morbi ultricies nunc eu tellus dignissim, eget venenatis dolor ullamcorper. Etiam dolor eros, iaculis at ultricies nec, volutpat nec orci. Vivamus tincidunt rutrum sapien, ac porttitor mauris tristique nec.</p>
      <p>Lorem ipsum dolor sit amet, consectetur adipiscing elit. Donec fringilla neque euismod volutpat cursus. Vestibulum ac pretium orci, consequat elementum velit. Etiam bibendum purus ac augue finibus volutpat. Vestibulum justo nisl, gravida aliquet sollicitudin ut, finibus vitae mi. Praesent aliquet scelerisque blandit. Sed id varius lacus, id tristique sem. Fusce et lobortis leo. Aliquam mollis pellentesque magna, condimentum ullamcorper ex ullamcorper non. Morbi ultricies nunc eu tellus dignissim, eget venenatis dolor ullamcorper. Etiam dolor eros, iaculis at ultricies nec, volutpat nec orci. Vivamus tincidunt rutrum sapien, ac porttitor mauris tristique nec.</p>
      <p>Lorem ipsum dolor sit amet, consectetur adipiscing elit. Donec fringilla neque euismod volutpat cursus. Vestibulum ac pretium orci, consequat elementum velit. Etiam bibendum purus ac augue finibus volutpat. Vestibulum justo nisl</p>
    </section>
  </main>
</body>
</html>
```